Solvane Holdings Inc. Business Card Design

My business is custom renovations and homes.I would need to have a new business logo created to go along with my company name. The business card should be of a modern style as this is the market I am focused on. I would need my contact information and website posted on the card. I would also like to list a few of the tasks I conduct on the card (such as: Renovations, Additions, Repairs, New Homes, Design, Consultations). On the reverse of the card I currently have just my logo and my motto, "Shaping Fresh Ground". However, I am open to completely changing everything as I am starting a new year and would like to excel further. Any new ideas and suggestions are always welcomed. Thank you.

Target Market(s)

Upscale residential and commercial renovations and builds

Industry/Entity Type

Business

Contact Information for Business Card

I would like the design to be able to be laser cut or burnt onto a wooden business card. I will be creating one option of cards for really loyal customers (wooden) and a second option for the everyday customer (paper).

Font styles to use
Other font styles liked:
• Calibri / anything of mordern taste

Colors
f37122
5c5c5c
474747
ffffff

Requirements
Must have
• I would like the colours of my business to be a sharp orange and grey. I believe this will symbolize a modern style. I am open to other suggestions if this is not suitable for the designers tastes. My contact info as follows:
• Dirk Malsworth
• President
• Solvane Holdings Inc.
• 555-239-7814
• dirk@solvaneholdings.example
• I would like my website (currently under construction) solvaneholdings.example on the card aswell.
Nice to have
• Along with a modern logo representing Solvane, I would like something on the card besides the logo and contact information. Perhaps a small background design. I feel it may be nice to have my services listed on the card (in smaller font on the bottom) Renovations, Additions, Repairs, Design, Consultations.
Should not have
• The business card should not have too many different colors. Should not have rounded corners.

```html
<!DOCTYPE html>
<html lang="en">
<head>
<meta charset="utf-8">
<title>Solvane Holdings Inc. — Business Card</title>
<link href="https://fonts.googleapis.com/css2?family=Carlito:wght@400;700&display=swap" rel="stylesheet">
<style>
  :root {
    --orange: #f37122;
    --grey-mid: #5c5c5c;
    --grey-dark: #474747;
    --panel: #3a3a3a;
    --panel-edge: #262626;
    --wood-light: #5a5a5a;
    --wood-dark: #1c1c1c;
    --white: #ffffff;
    --stage: #bdbdbd;
  }
  * { box-sizing: border-box; margin: 0; padding: 0; }
  html, body { width: 1200px; height: 837px; overflow: hidden; }
  body {
    background: var(--stage);
    font-family: "Carlito", "Calibri", sans-serif;
    position: relative;
  }
  .card {
    position: absolute;
    top: 275px;
    width: 500px;
    height: 286px;
    overflow: hidden;
    box-shadow: 0 6px 16px rgba(0,0,0,0.35);
  }
  .card--contact { left: 60px; }
  .card--brand { left: 640px; }
  .wood-texture {
    position: absolute;
    inset: 0;
    background:
      repeating-linear-gradient(90deg, rgba(0,0,0,0.25) 0 3px, transparent 3px 38px),
      linear-gradient(90deg, var(--wood-dark), var(--wood-light) 25%, #2a2a2a 45%, var(--wood-light) 70%, var(--wood-dark));
  }
  .panel {
    position: absolute;
    left: 38px;
    top: 30px;
    width: 424px;
    height: 226px;
    border-radius: 113px;
    background: linear-gradient(160deg, #444 0%, var(--panel) 55%, #333 100%);
    border: 7px solid var(--panel-edge);
    box-shadow: inset 0 2px 6px rgba(0,0,0,0.6), 0 1px 0 rgba(255,255,255,0.08);
    display: flex;
    flex-direction: column;
    justify-content: center;
    align-items: center;
    text-align: center;
    color: var(--white);
  }
  .person-name { font-size: 27px; font-weight: 700; line-height: 1; }
  .person-title { font-size: 16px; color: var(--orange); margin-bottom: 20px; }
  .contact-line { font-size: 16px; line-height: 1.3; }
  .contact-web { font-size: 16px; color: var(--orange); line-height: 1.3; }
  .brand-mark {
    display: flex; align-items: center; gap: 10px;
    font-size: 44px; font-weight: 700; color: var(--orange); line-height: 1;
  }
  .brand-mark__square { width: 18px; height: 18px; background: var(--orange); }
  .company-name { font-size: 22px; font-weight: 700; margin-top: 10px; line-height: 1; }
  .tagline { font-size: 9px; letter-spacing: 3px; margin-top: 4px; margin-bottom: 10px; }
  .services { font-size: 14px; line-height: 1.25; }
  .services .sep { color: var(--orange); padding: 0 3px; }
</style>
</head>
<body>
  <section class="card card--contact">
    <div class="wood-texture" role="img" aria-label="Dark grey wood grain texture"></div>
    <div class="panel">
      <p class="person-name">Dirk Malsworth</p>
      <p class="person-title">President</p>
      <p class="contact-line">555-239-7814</p>
      <p class="contact-line">dirk@solvaneholdings.example</p>
      <p class="contact-web">solvaneholdings.example</p>
    </div>
  </section>

  <section class="card card--brand">
    <div class="wood-texture" role="img" aria-label="Dark grey wood grain texture"></div>
    <div class="panel">
      <p class="brand-mark"><span class="brand-mark__square"></span>Solvane</p>
      <p class="company-name">Solvane Holdings Inc.</p>
      <p class="tagline">Shaping Fresh Ground</p>
      <p class="services">Renovations<span class="sep">|</span>Additions<span class="sep">|</span>Repairs<span class="sep">|</span>Design</p>
      <p class="services">Consultations</p>
    </div>
  </section>
</body>
</html>
```